Give my personal webpage more appeal!

I need my CV website improved - drmeganholt.com.au.
I am using the template KESTREL from pagecraftly. i would like to keep the already existing theme but am open to suggestions.
Please focus on imagery, colour scheme, and textures to enhance the appeal and look of the page.
The content is there, but now I need a designer to improve the look of my page.
I need styling, royalty-free unique modern images to make the page professional, personal and friendly.
I work in healthcare, so I'm a people person.
I teach professionals and I treat a lot of families.

Target Market(s)

Parents, Professional Healthcare providers

Number of Pages Required

1 page

Font styles to use
Serif
Sans Serif

Requirements
Must have
• My face - image at the top, all the information already contained in it.
• Links to the websites I manage such as my blog.
• One Page website.
• All the information it already contains with the ability to have more.
• Ideally, we would keep the same format for the page although I'm happy to expand column and change the page's structure with in the theme template KESTREL.
Nice to have
• The current KESTREL template. I would like to keep the already existing theme but am open to suggestions.
Should not have
• Multiple pages.

```html
<!DOCTYPE html>
<html lang="en">
<head>
<meta charset="utf-8">
<title>Dr Megan Holt – Chiropractor</title>
<link href="https://fonts.googleapis.com/css2?family=Open+Sans:wght@400;600;700&family=Roboto+Condensed:wght@300;400;700&display=swap" rel="stylesheet">
<style>
:root{
  --orange:#f2a81d;
  --orange-dark:#e29612;
  --grey:#7d7d7d;
  --grey-dark:#5b5b5d;
  --grey-light:#ededed;
  --text:#555;
  --white:#fff;
  --link:#2a9fd6;
  --head:'Roboto Condensed',Arial,sans-serif;
  --body:'Open Sans',Arial,sans-serif;
}
*{box-sizing:border-box;margin:0;padding:0}
html,body{width:1200px;height:5294px;overflow:hidden}
body{font-family:var(--body);color:var(--text);background:var(--white);font-size:13px;line-height:1.6}
.wrap{width:1044px;margin:0 auto;position:relative}
section,header,nav,footer{position:relative;width:1200px;overflow:hidden}
.section-title{font-family:var(--head);font-weight:400;font-size:44px;text-align:center;letter-spacing:1px;text-transform:uppercase}
.section-title .accent{color:var(--orange)}
.rule{width:60px;height:2px;background:currentColor;margin:6px auto 0;opacity:.7}
.pill{display:inline-block;border-radius:20px;font-family:var(--head);font-weight:700;font-size:15px;padding:9px 28px;letter-spacing:.5px}

/* top bar */
.topbar{height:35px;background:var(--grey-light)}
.topbar .wrap{display:flex;justify-content:space-between;align-items:center;height:35px}
.social{display:flex;gap:14px}
.dot{width:12px;height:12px;border-radius:50%;background:var(--orange);display:inline-block}
.topbar .mail{display:flex;align-items:center;gap:8px;color:var(--grey);font-size:12px}
/* header */
.masthead{height:89px}
.masthead .wrap{display:flex;justify-content:space-between;align-items:center;height:89px}
.brand{display:flex;align-items:center;gap:12px;font-family:var(--head);font-size:34px;font-weight:400;color:var(--orange);line-height:1}
.brand .dot{width:16px;height:16px}
.call{display:flex;align-items:center;gap:10px;font-family:var(--head);font-size:20px;color:var(--grey)}
.call b{color:var(--orange);font-size:26px}
/* nav */
.mainnav{height:60px;background:var(--orange)}
.mainnav ul{list-style:none;display:flex;height:60px;width:1044px;margin:0 auto}
.mainnav li{font-family:var(--head);color:var(--white);font-size:16px;padding:0 20px;display:flex;align-items:center;text-transform:uppercase}
.mainnav li.active{background:var(--grey)}
/* hero */
.hero{height:568px}
.hero-photo{position:absolute;inset:0;background:radial-gradient(circle at 72% 45%,#b8866d 0 14%,transparent 30%),linear-gradient(115deg,#5f8a3a,#b8c98a 40%,#e8efe0 60%,#7fa25a)}
.hero-text{position:absolute;left:78px;top:200px;color:var(--white)}
.hero-text h1{font-family:var(--head);font-weight:400;font-size:52px;letter-spacing:2px}
.hero-text p{font-size:22px;color:#fde7b0;margin:4px 0 26px}
.hero-text .pill{background:var(--orange);color:var(--white)}
/* about */
.about{height:370px;background:var(--orange);color:var(--white);text-align:center;padding-top:56px}
.about p{width:880px;margin:28px auto 22px;font-size:13px;line-height:1.75}
.about .pill{background:var(--white);color:var(--orange)}
/* skills */
.skills{height:759px;color:var(--white);padding-top:50px}
.skills-bg{position:absolute;inset:0;background:linear-gradient(160deg,#9a9a98,#7b7b79 55%,#6d6d6b)}
.skills .inner{position:relative}
.skill-grid{display:grid;grid-template-columns:repeat(3,1fr);row-gap:60px;margin-top:60px;text-align:center}
.skill .ic{width:118px;height:118px;border-radius:50%;background:var(--orange);border:6px solid #f6c35e;margin:0 auto 14px;display:flex;align-items:center;justify-content:center}
.skill h3{font-family:var(--head);font-weight:400;font-size:24px}
.skill p{width:260px;margin:4px auto 0;font-size:12.5px;line-height:1.5}
.skill p b{font-weight:600}
/* experiences */
.experience{height:608px;padding-top:48px}
.experience .section-title{color:var(--grey)}
.accordion{width:880px;margin:40px auto 36px;border:1px solid #ccc}
.acc-row{display:flex;justify-content:space-between;align-items:center;height:48px;padding:0 22px;border-top:1px solid #ddd;color:var(--grey)}
.acc-row:first-child{border-top:none}
.acc-row span{display:flex;align-items:center;gap:12px}
.acc-body{padding:6px 22px 22px;border-top:1px solid #ddd;font-size:12.5px;color:var(--text)}
.experience .center{text-align:center}
.experience .pill{background:var(--orange);color:var(--white)}
/* credentials */
.credentials{height:476px;color:var(--white)}
.cred-bg{position:absolute;inset:0;background:radial-gradient(circle at 45% 40%,#f7c04a,var(--orange) 55%,#e59a10)}
.credentials .inner{position:relative;padding-top:78px}
.credentials .intro{width:720px;margin:0 auto;text-align:center;font-size:13px}
.cred-grid{display:grid;grid-template-columns:1fr 1fr;row-gap:40px;margin:54px 0 0 0}
.cred{display:flex;gap:22px}
.cred .num{font-family:var(--head);font-size:30px;line-height:1}
.cred p{font-size:13px;line-height:1.5}
/* employment */
.employment{height:837px;background:var(--grey);color:var(--white);padding-top:48px}
.timeline{margin:40px 0 0 0;border-left:2px solid #bcbcbc;position:relative}
.job{padding:0 0 30px 0}
.job-head{display:flex;align-items:center;gap:44px;padding-left:16px}
.job h3{font-family:var(--body);font-weight:600;font-size:18px;line-height:1.25;width:250px}
.job .years{border:2px solid #d8d8d8;padding:4px 14px;font-family:var(--head);font-size:18px}
.job p{border-top:1px solid #a3a3a3;margin-top:10px;padding:8px 0 0 16px;font-size:12.5px;line-height:1.6;width:1010px}
/* sites */
.sites{height:328px;padding-top:48px}
.sites .section-title{color:var(--grey-dark)}
.site-row{display:flex;justify-content:space-between;align-items:center;margin-top:54px}
.site{width:210px;height:160px;display:flex;flex-direction:column;align-items:center;justify-content:center;gap:10px;font-family:var(--head);font-size:22px;color:var(--grey-dark)}
.site .sq{width:96px;height:96px;background:#1e2a3a}
.site .cc{width:88px;height:88px;border-radius:50%;background:#222}
/* contact */
.contact{height:406px;background:var(--orange);color:var(--white);padding-top:48px}
.contact form{display:grid;grid-template-columns:340px 620px;grid-template-rows:40px 40px 40px;gap:16px;margin:46px 0 0 48px}
.field{background:var(--white);height:40px;color:#aaa;padding:9px 14px;font-size:13px}
.f-name{grid-column:1;grid-row:1}
.f-mail{grid-column:1;grid-row:2}
.f-phone{grid-column:1;grid-row:3}
.msg{grid-column:2;grid-row:1 / span 2;height:96px}
.submit{grid-column:2;grid-row:3;background:var(--grey);color:var(--white);height:40px;font-family:var(--head);font-size:20px;text-align:center;padding-top:6px;letter-spacing:1px}
/* blog */
.blog{height:494px;padding-top:40px}
.blog .section-title{color:var(--grey)}
.blog-grid{display:grid;grid-template-columns:repeat(4,1fr);gap:28px;margin-top:40px}
.post .thumb{height:150px}
.post h4{color:var(--link);font-weight:400;font-size:13px;margin-top:10px;line-height:1.45}
.post .date{font-size:11px;color:var(--grey);margin:6px 0;display:flex;align-items:center;gap:6px}
.post p{font-size:13px;line-height:1.5}
/* footer */
.site-footer{height:264px;background:var(--grey);color:var(--white)}
.foot-top{display:flex;justify-content:space-between;align-items:center;height:64px;border-bottom:1px solid #9a9a9a}
.foot-top ul{list-style:none;display:flex;gap:30px;font-size:13px}
.foot-top .social .dot{background:var(--white);width:16px;height:16px}
.site-footer h5{font-family:var(--head);font-size:20px;font-weight:400;margin:14px 0 18px}
.foot-contact{display:flex;justify-content:space-between}
.fc{display:flex;align-items:center;gap:14px;font-size:13px;width:220px}
.fc .ci{width:42px;height:42px;border-radius:50%;background:var(--orange);display:flex;align-items:center;justify-content:center;flex:none}
.copyright{position:absolute;left:0;bottom:0;width:1200px;height:40px;background:var(--orange);text-align:center;font-size:12px;padding-top:10px}
</style>
</head>
<body>

<div class="topbar">
  <div class="wrap">
    <div class="social"><span class="dot"></span><span class="dot"></span></div>
    <div class="mail">
      <svg width="16" height="12" viewBox="0 0 16 12"><rect x="0.5" y="0.5" width="15" height="11" fill="none" stroke="#f2a81d"/><path d="M1 1l7 6 7-6" fill="none" stroke="#f2a81d"/></svg>
      Lorem Ipsum is simply
    </div>
  </div>
</div>

<header class="masthead">
  <div class="wrap">
    <div class="brand"><span class="dot"></span>Dr Megan Holt</div>
    <div class="call">
      Call us now
      <svg width="22" height="22" viewBox="0 0 24 24"><path d="M6.6 10.8a15 15 0 006.6 6.6l2.2-2.2c.3-.3.7-.4 1-.2 1.1.4 2.3.6 3.6.6.6 0 1 .4 1 1V20c0 .6-.4 1-1 1C10.6 21 3 13.4 3 4c0-.6.4-1 1-1h3.5c.6 0 1 .4 1 1 0 1.3.2 2.5.6 3.6.1.3 0 .7-.2 1z" fill="#f2a81d"/></svg>
      <b>123 456 7890</b>
    </div>
  </div>
</header>

<nav class="mainnav">
  <ul>
    <li class="active">About Me</li><li>Skills</li><li>Professional Experiences</li><li>Education</li><li>Employment</li><li>My Sites</li><li>Blog</li><li>Contact</li>
  </ul>
</nav>

<section class="hero">
  <div class="hero-photo" role="img" aria-label="Portrait photograph of Dr Megan Holt smiling in a red top, leafy green garden behind"></div>
  <div class="hero-text">
    <h1>DR MEGAN HOLT</h1>
    <p>Lorem Ipsum simply dummy text of the printing.</p>
    <span class="pill">CONTACT US NOW</span>
  </div>
</section>

<section class="about">
  <h2 class="section-title">About Me</h2>
  <div class="rule"></div>
  <p>Hello, I am a Chiropractor and a Diplomate of the Global Academy of Muscle Testing (GAMT). I am also on the board of certified teachers for the GAMT. Teaching engagements take me to local, national and international destinations. Thank you for visiting my page, I look forward to sharing some of my insights with you via my blog.<br>I am born and bred here in Brisbane, Australia and love this city that I call home.</p>
  <span class="pill">READ MORE »</span>
</section>

<section class="skills">
  <div class="skills-bg" role="img" aria-label="Soft grey backdrop of smooth spa stones resting on raked sand"></div>
  <div class="wrap inner">
    <h2 class="section-title">Skills</h2>
    <div class="skill-grid">
      <div class="skill">
        <div class="ic"><svg width="54" height="54" viewBox="0 0 54 54" fill="none" stroke="#fff" stroke-width="3"><path d="M6 48h42M12 44V30M22 44V22M32 44V26M42 44V14"/><path d="M10 24l12-10 10 6 12-12"/></svg></div>
        <h3>Business Development</h3>
        <p>I founded an award winning Chiropractic healthcare clinic in 2005. It grew to employ five... <b>READ MORE »</b></p>
      </div>
      <div class="skill">
        <div class="ic"><svg width="54" height="54" viewBox="0 0 54 54" fill="none" stroke="#fff" stroke-width="3"><path d="M8 22h8l20-12v34L16 32H8z"/><path d="M14 32l4 12h6l-3-12M42 20c3 3 3 11 0 14"/></svg></div>
        <h3>Teaching</h3>
        <p>I love the symbiotic relationship I have with my students. A room with eager minds eager to... <b>READ MORE »</b></p>
      </div>
      <div class="skill">
        <div class="ic"><svg width="54" height="54" viewBox="0 0 54 54" fill="none" stroke="#fff" stroke-width="3"><circle cx="27" cy="27" r="20"/><circle cx="27" cy="27" r="12"/><circle cx="27" cy="27" r="4" fill="#fff"/></svg></div>
        <h3>Chiropractic Skills</h3>
        <p>Diagnostics using functional neurology and manual muscle testing along with manual... <b>READ MORE »</b></p>
      </div>
      <div class="skill">
        <div class="ic"><svg width="54" height="54" viewBox="0 0 54 54"><path d="M27 46S8 34 8 20a10 10 0 0119-4 10 10 0 0119 4c0 14-19 26-19 26z" fill="#fff"/></svg></div>
        <h3>Mother and Wife</h3>
        <p>I am a wife of a wellness Chiropractor and mother of two, one was a bonus, and one that I birthed... <b>READ MORE »</b></p>
      </div>
      <div class="skill">
        <div class="ic"><svg width="54" height="54" viewBox="0 0 54 54" fill="none" stroke="#fff" stroke-width="3"><path d="M8 42l12-14 10 8 16-22"/><circle cx="20" cy="28" r="3" fill="#fff"/><circle cx="30" cy="36" r="3" fill="#fff"/><circle cx="46" cy="14" r="3" fill="#fff"/></svg></div>
        <h3>Product Launching</h3>
        <p>I have a special interest in product launching using the power of social media connectedness... <b>READ MORE »</b></p>
      </div>
      <div class="skill">
        <div class="ic"><svg width="54" height="54" viewBox="0 0 54 54" fill="none" stroke="#fff" stroke-width="3"><path d="M16 8h22c0 14-4 20-11 20S16 22 16 8zM27 28v16M18 46h18"/></svg></div>
        <h3>Event Co-Ordination</h3>
        <p>There's nothing quite like a deadline to get you focused, and events are like a deadline... <b>READ MORE »</b></p>
      </div>
    </div>
  </div>
</section>

<section class="experience">
  <h2 class="section-title">Professional <span class="accent">Experiences</span></h2>
  <div class="accordion">
    <div class="acc-row"><span><svg width="14" height="14" viewBox="0 0 14 14"><path d="M2 12l1-4 7-7 3 3-7 7z" fill="none" stroke="#999"/></svg>2017</span><span>⌃</span></div>
    <div class="acc-body">Started GutwiseOZ – Exclusive Distributors for Enterocalm (Queensland, New South Wales and Victoria). GutwiseOZ is sponsoring 'Movement for Every Body' for the GAMT in Adelaide in April.<br>Presenting Muscle Testing Certification Seminar – Sessions 7-8, Brisbane<br>Scheduled to present 'Early Reflex Integration' Seminars with founder Dr Colin Marsh DC in Sydney mid 2017</div>
    <div class="acc-row"><span><svg width="14" height="14" viewBox="0 0 14 14"><path d="M2 12l1-4 7-7 3 3-7 7z" fill="none" stroke="#999"/></svg>2016</span><span>+</span></div>
    <div class="acc-row"><span><svg width="14" height="14" viewBox="0 0 14 14"><path d="M2 12l1-4 7-7 3 3-7 7z" fill="none" stroke="#999"/></svg>2015</span><span>+</span></div>
    <div class="acc-row"><span><svg width="14" height="14" viewBox="0 0 14 14"><path d="M2 12l1-4 7-7 3 3-7 7z" fill="none" stroke="#999"/></svg>2014</span><span>+</span></div>
  </div>
  <div class="center"><span class="pill">VIEW ALL »</span></div>
</section>

<section class="credentials">
  <div class="cred-bg" role="img" aria-label="Warm orange backdrop with a soft, faded flower texture"></div>
  <div class="wrap inner">
    <p class="intro">Life is for learning. And the more I learn, the more curious I become. I have a thirst to understand things and am passionately inquisitive. My patients and my children are my greatest teachers. But here are my formal recognised studies.</p>
    <div class="cred-grid">
      <div class="cred"><span class="num">01</span><p>Diplomate Of The Global Council Of Muscle Testing<br>Board Of Certified Teachers<br>Antwerp, Belgium 2008</p></div>
      <div class="cred"><span class="num">02</span><p>Master Of Chiropractic<br>Sydney, Australia 2000-2002</p></div>
      <div class="cred"><span class="num">03</span><p>Bachelor Of Science (Anatomy)<br>Brisbane, Australia 1997-1999</p></div>
      <div class="cred"><span class="num">04</span><p>Ridgeview State High School<br>1992-1996</p></div>
    </div>
  </div>
</section>

<section class="employment">
  <h2 class="section-title">Employment</h2>
  <div class="rule"></div>
  <div class="wrap">
    <div class="timeline">
      <div class="job">
        <div class="job-head"><h3>Whole Body Care<br>Founder, Chiropractor</h3><span class="years">2005-2017</span></div>
        <p>What a wonderful place to work! I can't come to this clinic and not feel happy. It's decorated for the hundreds of children who get treated here. I've been privileged to watch so many families blossom through the stages of infancy to teens. They feel like family. My job here as Chiropractor has been to train my Chiropractic Associates, Chiropractic Assistants and support staff. To... READ MORE</p>
      </div>
      <div class="job">
        <div class="job-head"><h3>Harbourside Spine &amp;<br>Health Centre</h3><span class="years">2004-2005</span></div>
        <p>I learned a lot from my mentor Dr Lewis Ashcroft here. He taught me how to think like a business woman, which was exactly what I needed for my next move.</p>
      </div>
      <div class="job">
        <div class="job-head"><h3>Balanced Living Centre<br>Associate Chiropractor</h3><span class="years">2003-2004</span></div>
        <p>Working under Dr Colin Marsh has been the greatest gift I could have imagined first year out of University. He taught me his life's learnings and I have treasured them. He taught me that the greatest gift for any teacher is to have their students surpass them. He taught me how to be an ego free teacher, share my knowledge unreservedly with those who ask, and how to life without expectations. He shaped me into the practitioner and teacher I have become.</p>
      </div>
      <div class="job">
        <div class="job-head"><h3>Eastbridge University<br>Chiropractic Skills Tutor</h3><span class="years">2002</span></div>
        <p>What an honour to be invited to tutor and examine 2nd year Chiropractic Skills whilst in my final year of my Masters of Chiropractic. And what a delightful bunch of students we had that year too!</p>
      </div>
    </div>
  </div>
</section>

<section class="sites">
  <h2 class="section-title">My Sites</h2>
  <div class="wrap site-row">
    <div class="site"><span class="dot" style="width:20px;height:20px"></span>Megan's Blog</div>
    <div class="site"><span class="sq"></span>GutwiseOZ</div>
    <div class="site"><span class="cc"></span>kinelearn.com.au</div>
    <div class="site"><span class="cc" style="background:#555"></span>Reflex Integration</div>
  </div>
</section>

<section class="contact">
  <h2 class="section-title">Contact Us</h2>
  <div class="rule"></div>
  <div class="wrap">
    <form>
      <div class="field f-name">Name</div>
      <div class="field f-mail">E - Mail</div>
      <div class="field f-phone">Phone no.</div>
      <div class="field msg">Message</div>
      <div class="submit">SUBMIT</div>
    </form>
  </div>
</section>

<section class="blog">
  <h2 class="section-title">Recent <span class="accent">Blog</span></h2>
  <div class="wrap blog-grid">
    <article class="post">
      <div class="thumb" role="img" aria-label="Photo of a family relaxing together outdoors" style="background:linear-gradient(135deg,#e9dcc9,#b8c7d6)"></div>
      <h4>Lorem Ipsum is simply dummy text of the printing.</h4>
      <div class="date"><svg width="10" height="10" viewBox="0 0 10 10"><rect x=".5" y="1.5" width="9" height="8" fill="none" stroke="#f2a81d"/></svg>January 16, 2017</div>
      <p>Lorem Ipsum is simply dummy text of the printing and typesetting industry.</p>
    </article>
    <article class="post">
      <div class="thumb" role="img" aria-label="Photo of a glowing sunrise over calm water" style="background:radial-gradient(circle at 50% 60%,#f7f0c8,#3c7fa0 55%,#123347)"></div>
      <h4>Lorem Ipsum is simply dummy text of the printing.</h4>
      <div class="date"><svg width="10" height="10" viewBox="0 0 10 10"><rect x=".5" y="1.5" width="9" height="8" fill="none" stroke="#f2a81d"/></svg>January 16, 2017</div>
      <p>Lorem Ipsum is simply dummy text of the printing and typesetting industry.</p>
    </article>
    <article class="post">
      <div class="thumb" role="img" aria-label="Photo of children playing on green grass" style="background:linear-gradient(160deg,#c9e3f2,#8fb85c 60%,#5e8a33)"></div>
      <h4>Lorem Ipsum is simply dummy text of the printing.</h4>
      <div class="date"><svg width="10" height="10" viewBox="0 0 10 10"><rect x=".5" y="1.5" width="9" height="8" fill="none" stroke="#f2a81d"/></svg>January 16, 2017</div>
      <p>Lorem Ipsum is simply dummy text of the printing and typesetting industry.</p>
    </article>
    <article class="post">
      <div class="thumb" role="img" aria-label="Portrait photo of a smiling woman" style="background:linear-gradient(135deg,#f1e4d8,#c79a7e 60%,#7a5440)"></div>
      <h4>Lorem Ipsum is simply dummy text of the printing.</h4>
      <div class="date"><svg width="10" height="10" viewBox="0 0 10 10"><rect x=".5" y="1.5" width="9" height="8" fill="none" stroke="#f2a81d"/></svg>January 16, 2017</div>
      <p>Lorem Ipsum is simply dummy text of the printing and typesetting industry.</p>
    </article>
  </div>
</section>

<footer class="site-footer">
  <div class="wrap">
    <div class="foot-top">
      <ul><li>About Me</li><li>Professional Experiences</li><li>Education</li><li>Employment</li><li>My Sites</li><li>Blog</li><li>Contact</li></ul>
      <div class="social"><span class="dot"></span><span class="dot"></span><span class="dot"></span><span class="dot"></span></div>
    </div>
    <h5>Contact Us</h5>
    <div class="foot-contact">
      <div class="fc"><span class="ci"><svg width="18" height="18" viewBox="0 0 24 24"><path d="M12 2a7 7 0 00-7 7c0 5 7 13 7 13s7-8 7-13a7 7 0 00-7-7zm0 9.5A2.5 2.5 0 1112 6.5a2.5 2.5 0 010 5z" fill="#fff"/></svg></span>Lorem Ipsum is simply dummy text</div>
      <div class="fc"><span class="ci"><svg width="18" height="18" viewBox="0 0 24 24"><path d="M6.6 10.8a15 15 0 006.6 6.6l2.2-2.2c.3-.3.7-.4 1-.2 1.1.4 2.3.6 3.6.6.6 0 1 .4 1 1V20c0 .6-.4 1-1 1C10.6 21 3 13.4 3 4c0-.6.4-1 1-1h3.5c.6 0 1 .4 1 1 0 1.3.2 2.5.6 3.6.1.3 0 .7-.2 1z" fill="#fff"/></svg></span>123 456 7890</div>
      <div class="fc"><span class="ci"><svg width="18" height="18" viewBox="0 0 24 24"><rect x="4" y="3" width="16" height="18" rx="2" fill="#fff"/><rect x="7" y="6" width="10" height="5" fill="#f2a81d"/></svg></span>123 456 7890</div>
      <div class="fc"><span class="ci"><svg width="18" height="14" viewBox="0 0 16 12"><rect x="0.5" y="0.5" width="15" height="11" fill="#fff"/><path d="M1 1l7 6 7-6" fill="none" stroke="#f2a81d"/></svg></span>Lorem Ipsum is simply</div>
    </div>
  </div>
  <div class="copyright">© DR. MEGAN HOLT - 2017 , All Rights Reserved</div>
</footer>

</body>
</html>
```